Fundraising Company Needs a Brochure Design

We need a brochure design for a company that helps charities raise money. Our main product is selling art on easels to raise money for various charites. The brochure will have a total of four pages with the size being 8.5" X 11" for each page. All of text will be provided for the brochure. The front page should include our logo and a short intro. The second page will contain a summary along with how the easel program works. The third page will contain information about the companies and charities we work with and other ways we raise money for charities. The back page will contain three testimonials along with our mission/vision statement and our contact information. We also need to include a picture of the easel somewhere in the catalog. The color of our logo is orange and light green but the brochure doesn't need to contain those colors.
The brochure will be presented to major charities and local businesses alike.
It Company

```html
<!DOCTYPE html>
<html lang="en">
<head>
<meta charset="utf-8">
<title>Gifts for Good – Back Cover</title>
<link rel="stylesheet" href="https://fonts.googleapis.com/css2?family=Open+Sans:wght@300;400;600;700;800&display=swap">
<style>
  :root {
    --orange: #f39020;
    --orange-deep: #ec6f1c;
    --lime: #d2dd22;
    --olive: #b9c22a;
    --ring-fill: #b7c12c;
    --white: #ffffff;
    --ink: #111111;
    --grey: #7c7c7c;
    --green-brand: #5fae3a;
  }
  html, body { margin: 0; padding: 0; overflow: hidden; background: #ffffff; }
  .page {
    position: relative;
    width: 1200px;
    height: 857px;
    overflow: hidden;
    font-family: "Open Sans", Arial, sans-serif;
    background: var(--lime);
  }
  .backdrop { position: absolute; inset: 0; }

  .card {
    position: absolute;
    background: var(--white);
    border-radius: 10px;
    box-shadow: 0 3px 6px rgba(0,0,0,0.25);
  }
  .mission-card {
    left: 33px; top: -12px; width: 265px; height: 172px;
    transform: rotate(-1.5deg);
  }
  .mission-title {
    position: absolute; left: 24px; top: 42px; margin: 0;
    font-size: 26px; font-weight: 800; color: var(--orange-deep);
    letter-spacing: -0.3px;
  }
  .mission-text {
    position: absolute; left: 24px; top: 72px; width: 215px; margin: 0;
    font-size: 9.6px; line-height: 1.36; color: var(--orange);
  }
  .brand-card {
    left: 872px; top: -12px; width: 270px; height: 172px;
    transform: rotate(1.2deg);
  }
  .brand {
    position: absolute; left: 30px; top: 60px;
    display: flex; align-items: center; gap: 12px;
  }
  .brand-dot { width: 44px; height: 44px; border-radius: 50%; background: var(--orange); }
  .brand-name { font-size: 27px; font-weight: 800; color: var(--green-brand); letter-spacing: -0.5px; }

  .quote-text {
    position: absolute; margin: 0;
    font-size: 8.4px; line-height: 1.42; color: var(--white);
  }
  .quote-a { left: 190px; top: 289px; width: 190px; }
  .quote-b { left: 410px; top: 325px; width: 126px; }
  .quote-c { left: 66px; top: 396px; width: 158px; }

  .speaker { position: absolute; font-size: 8px; line-height: 1.2; color: var(--orange); }
  .speaker b { display: block; font-weight: 700; }
  .speaker-a { left: 246px; top: 411px; text-align: right; width: 76px; }
  .speaker-b { left: 457px; top: 414px; }
  .speaker-c { left: 247px; top: 510px; }

  .stray-label { position: absolute; left: 599px; top: 419px; font-size: 8px; color: var(--ink); }

  .contact-mark { position: absolute; left: 46px; top: 727px; width: 38px; height: 38px; background: var(--orange); }
  .contact-title { position: absolute; left: 97px; top: 752px; margin: 0; font-size: 13px; font-weight: 800; color: var(--ink); }
  .contact-text {
    position: absolute; left: 45px; top: 770px; width: 205px; margin: 0;
    font-size: 10.6px; line-height: 1.4; color: var(--ink);
  }

  .tagline {
    position: absolute; left: 627px; top: 719px; width: 560px; margin: 0;
    color: var(--grey); text-transform: uppercase;
  }
  .tagline-strong { font-size: 32.5px; font-weight: 800; line-height: 43px; letter-spacing: -0.2px; }
  .tagline-light { font-size: 14px; font-weight: 300; line-height: 20px; letter-spacing: 0; }
</style>
</head>
<body>
<main class="page">
  <svg class="backdrop" width="1200" height="857" viewBox="0 0 1200 857" aria-hidden="false">
    <defs>
      <linearGradient id="photoTones" x1="0" y1="0" x2="0" y2="1">
        <stop offset="0" stop-color="#8fa86a"/>
        <stop offset="0.22" stop-color="#6f5a3e"/>
        <stop offset="0.45" stop-color="#7fbf3a"/>
        <stop offset="0.7" stop-color="#6d5a44"/>
        <stop offset="1" stop-color="#4e3f30"/>
      </linearGradient>
    </defs>
    <rect class="sky-band" width="1200" height="857" fill="var(--orange)"/>
    <path class="olive-wave" d="M0,100 C180,40 420,60 600,170 C760,255 940,250 1200,195 V857 H0 Z" fill="var(--olive)"/>
    <path class="lime-wave" d="M0,172 C200,115 420,140 600,222 C760,290 960,295 1200,235 V857 H0 Z" fill="var(--lime)"/>
    <path class="photo" role="img" aria-label="Photo: four children smiling behind a wooden lemonade stand with a hand-painted sign"
          d="M598,226 C760,252 920,242 1200,222 V700 C1000,690 800,700 598,708 Z" fill="url(#photoTones)"/>

    <g class="testimonial-bubbles" fill="var(--orange)" stroke="var(--white)" stroke-width="2.5" stroke-linejoin="round">
      <path d="M188,276 H378 Q388,276 388,286 V404 L368,380 H188 Q178,380 178,370 V286 Q178,276 188,276 Z"/>
      <path d="M410,317 H533 Q543,317 543,327 V377 Q543,387 533,387 H420 L400,404 V327 Q400,317 410,317 Z"/>
      <path d="M65,388 H220 Q230,388 230,398 V494 L210,472 H65 Q55,472 55,462 V398 Q55,388 65,388 Z"/>
    </g>
    <g class="testimonial-portraits" fill="var(--ring-fill)" stroke="var(--white)" stroke-width="5">
      <circle cx="357" cy="427" r="24"/>
      <circle cx="421" cy="427" r="24"/>
      <circle cx="213" cy="522" r="24"/>
    </g>
  </svg>

  <section class="card mission-card">
    <h2 class="mission-title">MISSION/VISION</h2>
    <p class="mission-text">At Gifts for Good, our mission is to provide our partners with an opportunity to improve their communities, and support charitable causes using our unique, creative, and non-invasive fundraising activities.</p>
  </section>

  <div class="card brand-card">
    <div class="brand">
      <span class="brand-dot"></span>
      <span class="brand-name">Gifts for Good</span>
    </div>
  </div>

  <p class="quote-text quote-a">At Gifts for Good, our mission is to provide our partners with an opportunity to improve their communities, and support charitable causes using our unique, creative, and non-invasive fundraising activities.</p>
  <p class="quote-text quote-b">At Gifts for Good, our mission is to provide our partners with an opportunity to improve their communities, and</p>
  <p class="quote-text quote-c">At Gifts for Good, our mission is to provide our partners with an opportunity to improve their communities, and support charitable causes using our unique, creative, and non-invasive fundraising activities.</p>

  <div class="speaker speaker-a"><b>DANA HOLLIS</b>director<br>Brightday Ltd.</div>
  <div class="speaker speaker-b"><b>DANA HOLLIS</b>director<br>Brightday Ltd.</div>
  <div class="speaker speaker-c"><b>DANA HOLLIS</b>director<br>Brightday Ltd.</div>
  <div class="stray-label">director</div>

  <div class="contact-mark"></div>
  <h3 class="contact-title">CONACTS:</h3>
  <p class="contact-text">your fundraising event, offering products ranging in value from $10.00 up to $10,000. We even supply the bid sheets and cashiers, all at no cost outlay to you</p>

  <p class="tagline">
    <span class="tagline-strong">IT’S OUR FAMILIES, OUR FRIENDS, AND OUR NEIGHBOURS</span><span class="tagline-light"> that make communi-ties beautiful. When we join together to help those amongst us in need, a beautiful community can become a work of art.</span>
  </p>
</main>
</body>
</html>
```